New Business Card

Use website for color, logo and theme.

http://www.plumwickonline.com/

Back side of card should be programs listed on home page of website

1) Phone Number is (800) 555-0142 x23
2) Fax (240) 555-0187
3) Address is - 647 W Harlowe Street, Suite 312, Baltimore, MD 21201
4) NMLS #738516

```html
<!DOCTYPE html>
<html lang="en">
<head>
<meta charset="utf-8">
<title>Plumwick Financial Services – Business Card</title>
<link href="https://fonts.googleapis.com/css2?family=Fira+Sans:wght@400;500;700&display=swap" rel="stylesheet">
<style>
  :root {
    --canvas: #e9e6e1;
    --card-white: #ffffff;
    --brand-blue: #1b6db3;
    --band-blue: #1664a8;
    --band-blue-dark: #0f4f8a;
    --olive: #b5ab45;
    --ink: #1d1d1f;
    --gold: #e8c53a;
    --back-blue: #3f5d9e;
    --back-blue-deep: #2f4a86;
    --white: #ffffff;
  }
  * { box-sizing: border-box; margin: 0; padding: 0; }
  html, body { width: 1200px; height: 1023px; overflow: hidden; }
  body {
    background: var(--canvas);
    font-family: "Fira Sans", Arial, sans-serif;
    position: relative;
  }
  .card {
    position: absolute;
    left: 180px;
    width: 840px;
    height: 480px;
    border-radius: 22px;
    overflow: hidden;
    box-shadow: 0 6px 18px rgba(0,0,0,0.18);
  }
  .card--front { top: 21px; background: var(--card-white); }
  .card--back { top: 522px; background: linear-gradient(135deg, var(--back-blue-deep), var(--back-blue)); }

  /* Front */
  .identity {
    position: absolute; top: 34px; right: 48px; text-align: right;
    color: var(--ink);
  }
  .identity__name { font-size: 36px; font-weight: 700; color: var(--brand-blue); }
  .identity__role, .identity__license { font-size: 21px; line-height: 1.3; }
  .portrait {
    position: absolute; left: 330px; top: 120px; width: 370px; height: 250px;
    background: linear-gradient(180deg, #6b5a50 0%, #2c2c30 45%, #1b1c20 100%);
    border-radius: 120px 120px 0 0;
  }
  .brand {
    position: absolute; left: 40px; top: 168px; display: flex; align-items: center; gap: 14px;
  }
  .brand__mark { width: 58px; height: 58px; border-radius: 50%; background: var(--brand-blue); flex: none; }
  .brand__name { font-size: 20px; font-weight: 700; color: var(--olive); line-height: 1.15; width: 200px; }
  .contacts {
    position: absolute; left: 40px; top: 268px; list-style: none;
    font-size: 20px; color: var(--ink);
  }
  .contacts li { display: flex; align-items: center; gap: 10px; height: 27px; }
  .contacts svg { width: 18px; height: 18px; fill: var(--brand-blue); flex: none; }
  .band { position: absolute; left: 0; bottom: 0; width: 840px; height: 150px; }
  .address {
    position: absolute; left: 40px; bottom: 24px; color: var(--white);
    font-size: 22px; font-weight: 500;
  }

  /* Back */
  .family-photo {
    position: absolute; right: 0; top: 150px; width: 520px; height: 330px;
    background: radial-gradient(ellipse at 55% 45%, rgba(140,150,200,0.55), rgba(63,93,158,0) 70%);
  }
  .programs { position: absolute; left: 44px; top: 30px; color: var(--white); }
  .programs__heading { color: var(--gold); font-size: 24px; font-weight: 700; margin: 4px 0 3px; }
  .programs__list { list-style: none; font-size: 20px; line-height: 1.3; }
  .programs__list li { display: flex; align-items: center; gap: 10px; }
  .programs__list svg { width: 20px; height: 16px; flex: none; }
  .programs__list--plain li { padding-left: 30px; }
</style>
</head>
<body>
  <section class="card card--front">
    <div class="identity">
      <div class="identity__name">Marcus Ellery</div>
      <div class="identity__role">Owner</div>
      <div class="identity__license">NMLS #738516</div>
    </div>
    <div class="portrait" role="img" aria-label="Portrait photo of the owner in a dark suit"></div>
    <div class="brand">
      <span class="brand__mark"></span>
      <span class="brand__name">Plumwick Financial Services, Inc.</span>
    </div>
    <ul class="contacts">
      <li><svg viewBox="0 0 24 24"><path d="M6.6 10.8a15 15 0 0 0 6.6 6.6l2.2-2.2a1 1 0 0 1 1-.25 11 11 0 0 0 3.6.6 1 1 0 0 1 1 1V20a1 1 0 0 1-1 1A17 17 0 0 1 3 4a1 1 0 0 1 1-1h3.5a1 1 0 0 1 1 1 11 11 0 0 0 .6 3.6 1 1 0 0 1-.25 1z"/></svg>(800) 555-0142 x23</li>
      <li><svg viewBox="0 0 24 24"><path d="M6 2h12v6H6zM4 9h16a2 2 0 0 1 2 2v6h-4v5H6v-5H2v-6a2 2 0 0 1 2-2zm4 8v3h8v-3z"/></svg>(240) 555-0187</li>
      <li><svg viewBox="0 0 24 24"><path d="M2 5h20v14H2zm2 2v.5l8 5 8-5V7zm0 2.8V17h16V9.8l-8 5z"/></svg>info@plumwickonline.com</li>
      <li><svg viewBox="0 0 24 24"><path d="M12 2a10 10 0 1 0 0 20 10 10 0 0 0 0-20zm6.9 9h-3a15 15 0 0 0-1.3-6A8 8 0 0 1 18.9 11zM12 4.1c.9 1.3 1.7 3.7 1.9 6.9h-3.8c.2-3.2 1-5.6 1.9-6.9zM9.4 5a15 15 0 0 0-1.3 6h-3A8 8 0 0 1 9.4 5zM5.1 13h3a15 15 0 0 0 1.3 6 8 8 0 0 1-4.3-6zm6.9 6.9c-.9-1.3-1.7-3.7-1.9-6.9h3.8c-.2 3.2-1 5.6-1.9 6.9zm2.6-.9a15 15 0 0 0 1.3-6h3a8 8 0 0 1-4.3 6z"/></svg>www.plumwickonline.com</li>
    </ul>
    <svg class="band" viewBox="0 0 840 150" preserveAspectRatio="none" aria-hidden="true">
      <path d="M0 70 Q420 30 840 0 V150 H0 Z" fill="var(--olive)"/>
      <path d="M0 82 Q420 46 840 18 V150 H0 Z" fill="var(--band-blue)"/>
      <path d="M0 130 Q420 120 840 110 V150 H0 Z" fill="var(--band-blue-dark)" opacity="0.5"/>
    </svg>
    <div class="address">647 W Harlowe Street, Suite 312, Baltimore, MD 21201</div>
  </section>

  <section class="card card--back">
    <div class="family-photo" role="img" aria-label="Smiling family photo with blue overlay"></div>
    <div class="programs">
      <h2 class="programs__heading">Traditional Loan Programs</h2>
      <ul class="programs__list">
        <li><svg viewBox="0 0 20 16"><path d="M1 8l5 5L19 1" stroke="var(--gold)" stroke-width="3" fill="none"/></svg>FHA loans starting at 580 score</li>
        <li><svg viewBox="0 0 20 16"><path d="M1 8l5 5L19 1" stroke="var(--gold)" stroke-width="3" fill="none"/></svg>FHA 203k starting at 600 score</li>
        <li><svg viewBox="0 0 20 16"><path d="M1 8l5 5L19 1" stroke="var(--gold)" stroke-width="3" fill="none"/></svg>VA starting at 600 score (100% LTV)</li>
      </ul>
      <ul class="programs__list programs__list--plain"><li>All Conventional loan programs.</li></ul>
      <h2 class="programs__heading">Low Credit Score Programs</h2>
      <ul class="programs__list">
        <li><svg viewBox="0 0 20 16"><path d="M1 8l5 5L19 1" stroke="var(--gold)" stroke-width="3" fill="none"/></svg>500 score up to 70% LTV</li>
        <li><svg viewBox="0 0 20 16"><path d="M1 8l5 5L19 1" stroke="var(--gold)" stroke-width="3" fill="none"/></svg>540 score up to 75% LTV</li>
        <li><svg viewBox="0 0 20 16"><path d="M1 8l5 5L19 1" stroke="var(--gold)" stroke-width="3" fill="none"/></svg>580 score up to 96.5% LTV</li>
      </ul>
      <h2 class="programs__heading">Alternative Loan Programs</h2>
      <ul class="programs__list">
        <li><svg viewBox="0 0 20 16"><path d="M1 8l5 5L19 1" stroke="var(--gold)" stroke-width="3" fill="none"/></svg>Investor Fix &amp; Flip Rehab Loans</li>
        <li><svg viewBox="0 0 20 16"><path d="M1 8l5 5L19 1" stroke="var(--gold)" stroke-width="3" fill="none"/></svg>Investor Stated Loans</li>
      </ul>
      <ul class="programs__list programs__list--plain">
        <li>Foreign National Loans</li>
        <li>Limited Documentation Loans (1 year tax or W2)</li>
      </ul>
    </div>
  </section>
</body>
</html>
```